Tidal-Cup Coffee Kiosks Webdesign project

Tidal-Cup Coffee Kiosks provides coffee carts, kiosks, and/or drive thrus depending on location. At Tidal-Cup our company focuses on offering healthy snack & drink options for people on the go as well as nutritional coaching with our daily "Cup notes." We will provide some healthy snacks as well.

We offer all organic coffee & espresso drinks,100% real fruit & vegetable smoothies, protein shakes, and healthy breakfast/snack items.

I want "balance" to be a big theme in the website design. True well-being is a balance of body (health), mind (emotional well-being) and spirit (we are a Christian based company who loves and accepts all people, sexual orientation, religions, ect)

My parents are missionaries and founded the Nicaraguan organization "Bright Harvest Outreach Nicaragua" over 11 years ago ( www.brightharvestout.org ). Tidal-Cup plans to be a financial partner to their mission so 10% of profits or 2% of total revenue, whichever is greater will go to Bright Harvest and their church plants & medical/dental clinic. I want this and info about Bright Harvest to have a page on the website.
Updates

Target Market(s)

Ages 18-54 (target coffee customer).

Industry/Entity Type

Financial

Requirements
Must have
• -Home page
-Menu page
-Locations page/contact page
-Kiosk options page (cart, kiosk & drive thru descriptions, pics, traffic & location needs, ect)
-Fundraising/Bright Harvest Outreach Nicaragua page
Nice to have
• I have a logo designed that I attached. I would like the colors to be dark brown, light brown, and a lime green. My business card is also attached.

```html
<!DOCTYPE html>
<html lang="en">
<head>
<meta charset="utf-8">
<title>Tidal-Cup Coffee Kiosks</title>
<link href="https://fonts.googleapis.com/css2?family=Lato:ital,wght@0,400;0,700;0,900;1,400&family=Kaushan+Script&display=swap" rel="stylesheet">
<style>
:root{
  --green:#6fb52c;
  --green-dark:#4f8f1c;
  --orange:#e8861a;
  --brown-dark:#2a140b;
  --brown:#3a1f12;
  --peach:#fde3c8;
  --cream:#fdf5ee;
  --text:#222;
  --muted:#666;
  --white:#fff;
}
*{box-sizing:border-box;margin:0;padding:0}
html,body{width:1200px;height:2640px;overflow:hidden;background:var(--white)}
body{position:relative;font-family:'Lato',sans-serif;color:var(--text)}
.abs{position:absolute}

/* header */
.hero{left:0;top:0;width:1200px;height:643px;background:radial-gradient(ellipse at 75% 45%,#b48d6c 0%,#d9c2ab 30%,#ece4dc 60%,#cfc4b8 100%)}
.nav{left:0;top:0;width:1200px;height:91px;background:linear-gradient(180deg,#7cc133,#5fa224)}
.nav-group{display:flex;position:absolute;top:20px}
.nav-group.left{left:110px;gap:58px}
.nav-group.right{left:700px;gap:58px}
.nav-item{text-align:center;color:var(--white);white-space:nowrap}
.nav-item b{display:block;font-weight:900;font-size:19px;letter-spacing:.5px}
.nav-item i{display:block;font-family:'Kaushan Script',cursive;font-style:normal;font-size:14px;margin-top:2px;color:#f1f9e6}
.brand{left:516px;top:0;width:168px;height:132px;background:var(--orange);display:flex;align-items:center;justify-content:center;flex-direction:column;gap:8px}
.brand-name{font-family:'Lato',sans-serif;font-weight:900;font-size:26px;color:var(--white)}
.brand-dot{width:16px;height:16px;border-radius:50%;background:var(--white)}
.hero-caption{left:127px;top:317px}
.hero-title{background:var(--white);display:inline-block;padding:12px 20px;font-weight:900;font-size:28px;color:var(--brown)}
.hero-sub{background:var(--white);margin-top:6px;padding:10px 20px;font-weight:700;font-size:13px;width:560px;color:var(--brown)}

/* menu band */
.band{left:0;top:643px;width:1200px;height:144px;background:var(--brown-dark);text-align:center;color:var(--white)}
.band h2{margin-top:48px;font-weight:900;font-size:28px;letter-spacing:3px}
.band p{font-family:'Kaushan Script',cursive;font-size:24px;margin-top:2px}
.intro{left:130px;top:832px;width:940px;text-align:center;font-size:18px;line-height:26px;color:var(--text)}
.tabs{left:113px;top:922px;width:955px;height:30px;display:flex;justify-content:space-between}
.tab{font-weight:900;font-size:17px;color:var(--orange);white-space:nowrap;line-height:24px}
.tab.active{color:var(--green);border-bottom:2px solid var(--green)}

.menu-grid{left:113px;top:984px;display:grid;grid-template-columns:470px 453px;column-gap:27px;row-gap:19px}
.item{display:flex;height:115px;background:var(--cream)}
.item-photo{width:115px;height:115px;background:radial-gradient(circle at 45% 55%,#2b150a 0%,#6b4128 35%,#e9e2db 60%,#fff 100%)}
.item-body{flex:1;padding:12px 10px 0 12px}
.item-name{font-weight:900;font-size:13px;margin-bottom:6px}
.item-desc{font-weight:700;font-size:12px;line-height:16px}
.price{width:110px;background:var(--peach);text-align:center;padding-top:24px;color:var(--brown)}
.price b{display:block;font-weight:900;font-size:21px}
.price span{display:block;font-weight:700;font-size:27px;margin-top:2px}

.pager{left:905px;top:1790px;display:flex;align-items:center;gap:8px}
.pager .dot{width:13px;height:13px;border-radius:50%;background:var(--brown)}
.pager .dot.on{background:var(--green);border:3px solid #cfe8b6}

/* testimonials */
.section-title{font-weight:900;font-size:15px;letter-spacing:.5px;color:var(--brown);white-space:nowrap}
.testimonials{left:113px;top:1903px;width:680px}
.quote{position:relative;margin-left:7px;border:3px solid var(--green);padding:14px 16px;font-style:italic;font-size:12px;line-height:18px;color:var(--muted)}
.quote::after{content:"";position:absolute;right:140px;bottom:-16px;width:26px;height:26px;background:var(--white);border-right:3px solid var(--green);border-bottom:3px solid var(--green);transform:skewX(40deg)}
.author{text-align:right;margin:18px 0 18px;padding-right:100px;font-size:13px;line-height:16px}
.author b{font-weight:700;display:block}
.author span{color:var(--green);font-size:12px}

.vote{left:845px;top:1903px;width:220px}
.vote .section-title{font-size:13px;letter-spacing:0}
.vote-text{margin-top:18px;font-size:12px;line-height:17px;color:var(--muted)}
.poll{margin-top:40px;list-style:none}
.poll li{display:flex;align-items:center;height:38px;font-size:13px}
.radio{width:20px;height:20px;border-radius:50%;background:#e7e7e7;margin-right:12px;border:1px solid #d3d3d3}
.poll li span.label{flex:1}
.count{background:var(--green);color:var(--white);font-weight:700;font-size:12px;width:42px;height:18px;border-radius:9px;text-align:center;line-height:18px}
.poll-rule{height:2px;background:var(--green);margin-top:6px}
.vote-actions{margin-top:24px;display:flex;align-items:center;gap:22px}
.vote-btn{background:var(--green);color:var(--white);font-weight:700;font-size:13px;width:88px;height:30px;line-height:30px;text-align:center}
.no-thanks{font-size:14px;text-decoration:underline;color:var(--text)}

/* footer */
.footer{left:0;top:2316px;width:1200px;height:283px;background:var(--brown-dark);color:var(--white)}
.foot-about{position:absolute;left:113px;top:28px;width:300px}
.foot-about h3{font-weight:400;font-size:23px}
.foot-about h4{color:var(--orange);font-weight:400;font-size:16px;line-height:19px;margin-top:4px}
.foot-about p{font-size:12px;line-height:16px;margin-top:12px}
.foot-title{color:var(--orange);font-weight:900;font-size:13px;letter-spacing:.5px}
.foot-offers{position:absolute;left:480px;top:32px;width:245px}
.foot-offers ul{list-style:none;margin-top:12px}
.foot-offers li{font-size:13px;height:38px;line-height:38px;border-bottom:1px dashed #6b5448}
.foot-news{position:absolute;left:809px;top:32px;width:255px}
.foot-news p{font-size:12px;margin-top:8px}
.email{margin-top:12px;height:32px;background:#3d2418;font-size:12px;line-height:32px;padding-left:10px;color:#bfb0a6}
.fine{font-size:9px;line-height:12px;color:#a8968b;margin-top:10px}
.socials{display:flex;gap:8px;margin-top:14px}
.socials span{width:40px;height:36px;background:#4a3024}
.legal{left:113px;top:2610px;font-size:11px;font-weight:700}
</style>
</head>
<body>

<div class="abs hero" role="img" aria-label="Photo of creamy coffee drinks topped with whipped cream and cocoa"></div>

<nav class="abs nav">
  <div class="nav-group left">
    <div class="nav-item"><b>HOME</b><i>take at home</i></div>
    <div class="nav-item"><b>MENU</b><i>food &amp; nutrition</i></div>
    <div class="nav-item"><b>ABOUT US</b><i>who we are</i></div>
  </div>
  <div class="nav-group right">
    <div class="nav-item"><b>KIOSKS</b><i>more from us</i></div>
    <div class="nav-item"><b>BRIGHT HARVEST</b><i>fundraising</i></div>
    <div class="nav-item"><b>CONTACT</b><i>write us</i></div>
  </div>
</nav>
<div class="abs brand"><span class="brand-dot"></span><span class="brand-name">Tidal-Cup</span></div>

<div class="abs hero-caption">
  <div class="hero-title">FRESH AND DELICIOUS TASTES</div>
  <div class="hero-sub">Lorem ipsum dolor sit amet, consectetuer adipiscing elit dipiscing elit</div>
</div>

<section class="abs band">
  <h2>MENU</h2>
  <p>View our delicious menu</p>
</section>

<p class="abs intro">Lorem ipsum dolor sit amet, consectetuer adipiscing elit, sed diam nonummy nibh euismod tincidunt ut laoreet dolore magna aliquam erat volutpat.</p>

<div class="abs tabs">
  <span class="tab active">COFFEE &amp; SMOOTHIES</span>
  <span class="tab">TEAS &amp; CHAI</span>
  <span class="tab">BREAKFAST &amp; LUNCH</span>
  <span class="tab">SEASONAL LATTE'S</span>
  <span class="tab">OUR SPECIAL COFFEE</span>
</div>

<div class="abs menu-grid">
  <article class="item"><div class="item-photo" role="img" aria-label="Cup of americano coffee"></div><div class="item-body"><div class="item-name">AMERICANO COFFEE</div><div class="item-desc">Lorem ipsum dolor sit amet, consectetuer adipiscing elit, sed diam nonummy nibh euismod tincidunt ut laoreet dolore magna aliquam erat</div></div><div class="price"><b>PRICE:</b><span>$4.99</span></div></article>
  <article class="item"><div class="item-photo" role="img" aria-label="Cup of americano coffee"></div><div class="item-body"><div class="item-name">AMERICANO COFFEE</div><div class="item-desc">Lorem ipsum dolor sit amet, consectetuer adipiscing elit, sed diam nonummy nibh euismod tincidunt ut laoreet dolore magna aliquam erat</div></div><div class="price"><b>PRICE:</b><span>$4.99</span></div></article>
  <article class="item"><div class="item-photo" role="img" aria-label="Cup of americano coffee"></div><div class="item-body"><div class="item-name">AMERICANO COFFEE</div><div class="item-desc">Lorem ipsum dolor sit amet, consectetuer adipiscing elit, sed diam nonummy nibh euismod tincidunt ut laoreet dolore magna aliquam erat</div></div><div class="price"><b>PRICE:</b><span>$4.99</span></div></article>
  <article class="item"><div class="item-photo" role="img" aria-label="Cup of americano coffee"></div><div class="item-body"><div class="item-name">AMERICANO COFFEE</div><div class="item-desc">Lorem ipsum dolor sit amet, consectetuer adipiscing elit, sed diam nonummy nibh euismod tincidunt ut laoreet dolore magna aliquam erat</div></div><div class="price"><b>PRICE:</b><span>$4.99</span></div></article>
  <article class="item"><div class="item-photo" role="img" aria-label="Cup of americano coffee"></div><div class="item-body"><div class="item-name">AMERICANO COFFEE</div><div class="item-desc">Lorem ipsum dolor sit amet, consectetuer adipiscing elit, sed diam nonummy nibh euismod tincidunt ut laoreet dolore magna aliquam erat</div></div><div class="price"><b>PRICE:</b><span>$4.99</span></div></article>
  <article class="item"><div class="item-photo" role="img" aria-label="Cup of americano coffee"></div><div class="item-body"><div class="item-name">AMERICANO COFFEE</div><div class="item-desc">Lorem ipsum dolor sit amet, consectetuer adipiscing elit, sed diam nonummy nibh euismod tincidunt ut laoreet dolore magna aliquam erat</div></div><div class="price"><b>PRICE:</b><span>$4.99</span></div></article>
  <article class="item"><div class="item-photo" role="img" aria-label="Cup of americano coffee"></div><div class="item-body"><div class="item-name">AMERICANO COFFEE</div><div class="item-desc">Lorem ipsum dolor sit amet, consectetuer adipiscing elit, sed diam nonummy nibh euismod tincidunt ut laoreet dolore magna aliquam erat</div></div><div class="price"><b>PRICE:</b><span>$4.99</span></div></article>
  <article class="item"><div class="item-photo" role="img" aria-label="Cup of americano coffee"></div><div class="item-body"><div class="item-name">AMERICANO COFFEE</div><div class="item-desc">Lorem ipsum dolor sit amet, consectetuer adipiscing elit, sed diam nonummy nibh euismod tincidunt ut laoreet dolore magna aliquam erat</div></div><div class="price"><b>PRICE:</b><span>$4.99</span></div></article>
  <article class="item"><div class="item-photo" role="img" aria-label="Cup of americano coffee"></div><div class="item-body"><div class="item-name">AMERICANO COFFEE</div><div class="item-desc">Lorem ipsum dolor sit amet, consectetuer adipiscing elit, sed diam nonummy nibh euismod tincidunt ut laoreet dolore magna aliquam erat</div></div><div class="price"><b>PRICE:</b><span>$4.99</span></div></article>
  <article class="item"><div class="item-photo" role="img" aria-label="Cup of americano coffee"></div><div class="item-body"><div class="item-name">AMERICANO COFFEE</div><div class="item-desc">Lorem ipsum dolor sit amet, consectetuer adipiscing elit, sed diam nonummy nibh euismod tincidunt ut laoreet dolore magna aliquam erat</div></div><div class="price"><b>PRICE:</b><span>$4.99</span></div></article>
  <article class="item"><div class="item-photo" role="img" aria-label="Cup of americano coffee"></div><div class="item-body"><div class="item-name">AMERICANO COFFEE</div><div class="item-desc">Lorem ipsum dolor sit amet, consectetuer adipiscing elit, sed diam nonummy nibh euismod tincidunt ut laoreet dolore magna aliquam erat</div></div><div class="price"><b>PRICE:</b><span>$4.99</span></div></article>
  <article class="item"><div class="item-photo" role="img" aria-label="Cup of americano coffee"></div><div class="item-body"><div class="item-name">AMERICANO COFFEE</div><div class="item-desc">Lorem ipsum dolor sit amet, consectetuer adipiscing elit, sed diam nonummy nibh euismod tincidunt ut laoreet dolore magna aliquam erat</div></div><div class="price"><b>PRICE:</b><span>$4.99</span></div></article>
</div>

<div class="abs pager">
  <svg width="12" height="14" viewBox="0 0 12 14"><path d="M11 1 L2 7 L11 13 Z" fill="#2a140b"/></svg>
  <span class="dot on"></span><span class="dot"></span><span class="dot"></span><span class="dot"></span><span class="dot"></span>
  <svg width="12" height="14" viewBox="0 0 12 14"><path d="M1 1 L10 7 L1 13 Z" fill="#2a140b"/></svg>
</div>

<section class="abs testimonials">
  <h3 class="section-title">TESTIMONIALS</h3>
  <div style="margin-top:30px">
    <blockquote class="quote">"Lorem ipsum dolor sit amet, consectetuer adipiscing elit, sed diam nonummy nibh euismod tincidunt ut laoreet dolore magna aliquam erat volutpat. Lorem ipsum dolor sit amet, consectetuer adipiscing elit, sed diam nonummy nibh euismod tincidunt ut laoreet dolore magna aliquam erat volutpat. "</blockquote>
    <div class="author"><b>DARIO MONTES</b><span>Manager</span></div>
    <blockquote class="quote">"Lorem ipsum dolor sit amet, consectetuer adipiscing elit, sed diam nonummy nibh euismod tincidunt ut laoreet dolore magna aliquam erat volutpat. Lorem ipsum dolor sit amet, consectetuer adipiscing elit, sed diam nonummy nibh euismod tincidunt ut laoreet dolore magna aliquam erat volutpat. "</blockquote>
    <div class="author"><b>DARIO MONTES</b><span>Manager</span></div>
  </div>
</section>

<aside class="abs vote">
  <h3 class="section-title">VOTE FOR AMERICANO COFFEE</h3>
  <p class="vote-text">Lorem ipsum dolor sit amet, consectetuer adipiscing elit, sed diam nonummy nibh euismod tincidunt ut laoreet dolore magna aliquam erat volutpat.</p>
  <ul class="poll">
    <li><span class="radio"></span><span class="label">Oh, it's very nice!</span><span class="count">12</span></li>
    <li><span class="radio"></span><span class="label">So-so</span><span class="count">206</span></li>
    <li><span class="radio"></span><span class="label">I don't known</span><span class="count">29</span></li>
    <li><span class="radio"></span><span class="label">It's very bad</span><span class="count">206</span></li>
  </ul>
  <div class="poll-rule"></div>
  <div class="vote-actions"><span class="vote-btn">VOTE</span><span class="no-thanks">No, thanks</span></div>
</aside>

<footer class="abs footer">
  <div class="foot-about">
    <h3>Sed ut perspiciatis und!</h3>
    <h4>At vero eos et accusamus et iusto odio dignissimos ducimus qui blanditis</h4>
    <p>Sed ut perspiciatis unde omnis iste natus error sit voluptatem accusantium doloremque laudantium, totam rem aperiam, eaque ipsa quae ab illo inventore veritatis et quasi architecto beatae vitae dicta sunt explicabo.</p>
    <p>Nemo enim ipsam voluptatem quia voluptas sit aspernatur aut odit aut fugit, sed quia</p>
  </div>
  <div class="foot-offers">
    <h3 class="foot-title">LATEST OFFERS</h3>
    <ul>
      <li>Lorem ipsum doloreem</li>
      <li>At Vero et iusto dignizzimos</li>
      <li>Voluptatum</li>
      <li>Sereno template</li>
      <li>Corrupti Data</li>
    </ul>
  </div>
  <div class="foot-news">
    <h3 class="foot-title">NEWSLETTER</h3>
    <p>Iste natus error sit voluptatem accusantium</p>
    <div class="email">e-mail *</div>
    <p class="fine">** Nemo enim ipsam voluptatem quia voluptas sit aspernatur aut odit aut fugit, sed quia.</p>
    <h3 class="foot-title" style="margin-top:16px">SOCIALS</h3>
    <div class="socials"><span></span><span></span><span></span><span></span><span></span></div>
  </div>
</footer>

<div class="abs legal">2015 Terms and conditions</div>

</body>
</html>
```